Business card for Crestline Bathrooms

Please design a business card for our bathroom renovation business. You can use my existing logo, but if you have an idea to modernize it, I would like to see it. Please see attached files first. I would like to use the blue and the orange theme. I like the concept of using the shower head in the logo. Please find following a design (or two) that I have been trying to create with my limited resources. That design was for a sign, but I was going to adopt it and use it as a business card as well. I like the concept of the water splash but I don’t think it “flows” nicely together with the logo. Another thought is that maybe creating the logo out of water splash could work and have a dramatic effect (like the water text and the butterfly picture attached with similar background instead of white). If the above doesn’t work I would like to see a modern simplified design. One of the attached files named as the unwanted business card has all the details that I want included in the business card. Please note that it is two sided.
Updates

I am very thankful for the designs that I have received, but they are very similar and only a couple of attempts to do something with the water splash as per my original brief. Modernizing the logo and having it made out of out of water splash with the orange as color accent could work and have a dramatic effect (like the water text and the butterfly picture attached with similar background instead of white). Please do not use the butterfly itself! This is just an example that images can be created out of water splash.

Contact Information for Business Card

all the details are on the unwonted business card file included

Colors
3176b5

Requirements
Nice to have
• Copied from the brief:
• ... maybe creating the logo out of water splash could work and have a dramatic effect (like the water text and the butterfly picture attached with similar background instead of white). Please do not use the butterfly itself!
Should not have
• I am getting designs with a butterfly. The butterfly picture was an example of creating something from a water splash. The butterfly itself has no association with anything other than the concept of creating a logo out of water splash. Sorry, I thought I was clear in the brief.

```html
<!DOCTYPE html>
<html lang="en">
<head>
<meta charset="utf-8">
<title>Crestline Bathrooms – Business Card</title>
<link rel="stylesheet" href="https://fonts.googleapis.com/css2?family=Arimo:wght@400;700&display=swap">
<style>
  :root {
    --backdrop: #1d3a57;
    --card-top: #ffffff;
    --card-bottom: #e6f0f9;
    --brand-blue: #3176b5;
    --ink: #17324d;
    --accent: #e8812b;
    --shadow: rgba(0, 0, 0, 0.45);
  }
  * { margin: 0; padding: 0; box-sizing: border-box; }
  html, body { width: 1200px; height: 900px; overflow: hidden; }
  body {
    background: var(--backdrop);
    font-family: "Arimo", Arial, sans-serif;
    color: var(--ink);
    position: relative;
  }
  .card {
    position: absolute;
    left: 330px;
    width: 556px;
    height: 343px;
    background: linear-gradient(180deg, var(--card-top) 0%, var(--card-bottom) 100%);
    box-shadow: 3px 4px 8px var(--shadow);
    overflow: hidden;
  }
  .card--front { top: 90px; }
  .card--back { top: 470px; }
  .card__band {
    position: absolute;
    left: 0; right: 0; bottom: 0;
    height: 8px;
    background: var(--accent);
  }

  /* Front */
  .brand {
    position: absolute;
    left: 26px;
    top: 146px;
    width: 220px;
    text-align: center;
  }
  .brand__name {
    font-size: 38px;
    font-weight: 400;
    letter-spacing: 0.5px;
    line-height: 1;
    color: var(--brand-blue);
  }
  .brand__sub {
    margin-top: 12px;
    display: flex;
    align-items: center;
    gap: 8px;
    font-size: 16px;
    letter-spacing: 2px;
    color: var(--ink);
  }
  .brand__sub::before, .brand__sub::after {
    content: "";
    flex: 1;
    height: 1px;
    background: var(--accent);
  }
  .divider {
    position: absolute;
    left: 267px;
    top: 102px;
    width: 2px;
    height: 140px;
    background: var(--accent);
  }
  .contact {
    position: absolute;
    left: 281px;
    top: 100px;
  }
  .contact__name {
    font-size: 19px;
    font-weight: 700;
    letter-spacing: 0.3px;
    margin-bottom: 14px;
    color: var(--brand-blue);
  }
  .contact__list { list-style: none; font-size: 15px; line-height: 20px; }
  .contact__item { display: flex; align-items: center; gap: 5px; }
  .contact__item svg { width: 11px; height: 11px; flex: none; color: var(--accent); }
  .contact__address { margin-top: 10px; font-size: 15px; }

  /* Back */
  .services {
    position: absolute;
    top: 96px;
    left: 0;
    width: 100%;
    text-align: center;
    list-style: none;
    font-size: 13.5px;
    line-height: 23px;
    letter-spacing: 0.3px;
  }
  .rule {
    position: absolute;
    left: 62px;
    right: 58px;
    top: 210px;
    height: 1px;
    background: var(--accent);
  }
  .badge { position: absolute; background: var(--brand-blue); }
  .badge--member { left: 77px; top: 230px; width: 80px; height: 88px; border-radius: 22px; }
  .badge--builders { left: 189px; top: 236px; width: 60px; height: 74px; }
</style>
</head>
<body>
  <section class="card card--front" aria-label="Business card front">
    <div class="brand">
      <div class="brand__name">Crestline</div>
      <div class="brand__sub">Bathrooms</div>
    </div>
    <div class="divider"></div>
    <div class="contact">
      <div class="contact__name">DANIEL MAROVIC</div>
      <ul class="contact__list">
        <li class="contact__item">
          <svg viewBox="0 0 12 12" aria-hidden="true"><path d="M1 4c0-2 2-3 5-3s5 1 5 3l-2 1-1-1.5H4L3 5z M2.5 6h7l1 5h-9z" fill="currentColor"/></svg>
          0412 555 208
        </li>
        <li class="contact__item">
          <svg viewBox="0 0 12 12" aria-hidden="true"><rect x="3" y="0.5" width="6" height="11" rx="1.2" fill="none" stroke="currentColor" stroke-width="1.3"/></svg>
          6200 4417
        </li>
        <li class="contact__item">
          <svg viewBox="0 0 12 12" aria-hidden="true"><rect x="0.5" y="2" width="11" height="8" fill="currentColor"/><path d="M1 2.5l5 4 5-4" stroke="#ffffff" fill="none"/></svg>
          daniel@crestlinebathrooms.com.au
        </li>
        <li class="contact__item">
          <svg viewBox="0 0 12 12" aria-hidden="true"><circle cx="6" cy="6" r="5.5" fill="currentColor"/></svg>
          crestlinebathrooms.com.au
        </li>
      </ul>
      <div class="contact__address">PO Box 41 Hillcrest 2620</div>
    </div>
    <div class="card__band"></div>
  </section>

  <section class="card card--back" aria-label="Business card back">
    <ul class="services">
      <li>COMPLETE BATHROOM RENOVATIONS &amp; REMODELLING</li>
      <li>HIGHLY SKILLED &amp; QUALIFIED TRADESPEOPLE</li>
      <li>PROFESSIONAL SERVICE FROM CONCEPT TO COMPLETION</li>
      <li>ALL WORK GUARANTEED</li>
    </ul>
    <div class="rule"></div>
    <div class="badge badge--member" role="img" aria-label="Industry association membership badge"></div>
    <div class="badge badge--builders" role="img" aria-label="Builders association membership badge"></div>
    <div class="card__band"></div>
  </section>
</body>
</html>
```